Clean bold and classy business card front and back
Rin can be the logo
My name Dorian Hesketh as owner
Phone email and address
Owner Dorian Hesketh
Phone 8505550147
Email ridgelineinsulate@mailbox.test
Address170 frank pais rd Fenwick fl 32390

Industry/Entity Type

Business

Contact Information for Business Card

Owner Dorian Hesketh
Phone 8505550147

Requirements
Must have
• Ridgeline insulate co under Rin logo
Nice to have
• Bold and clean. Maybe use Rin as logo and name under it. Have logo on one side and info on the other side with logo also
• Put a pic up. It doesn't have to be that but something that can be used
• Try some fancy fonts also

```html
<!DOCTYPE html>
<html lang="en">
<head>
<meta charset="utf-8">
<title>Ridgeline Insulate Co — Business Card</title>
<link href="https://fonts.googleapis.com/css2?family=Open+Sans:wght@400;600;800&display=swap" rel="stylesheet">
<style>
  :root {
    --backdrop: #8f8f8f;
    --brand-blue: #0c78c2;
    --ink-black: #050505;
    --accent-orange: #f26a1b;
    --paper-white: #ffffff;
  }
  * { box-sizing: border-box; margin: 0; padding: 0; }
  html, body {
    width: 1200px; height: 900px; overflow: hidden;
    background: var(--backdrop);
    font-family: "Open Sans", Arial, sans-serif;
  }
  .canvas {
    position: relative; width: 1200px; height: 900px;
    display: flex; flex-direction: column; align-items: center;
    justify-content: center; gap: 48px;
  }
  .card {
    position: relative; width: 640px; height: 366px;
    overflow: hidden; color: var(--paper-white);
    box-shadow: 0 6px 18px rgba(0,0,0,0.25);
  }
  .card--front { background: var(--brand-blue); }
  .card--back { background: var(--brand-blue); }

  .wordmark { position: absolute; display: flex; flex-direction: column; line-height: 1; }
  .wordmark__name {
    font-weight: 800; letter-spacing: 4px;
  }
  .wordmark__tagline { font-weight: 600; margin-top: 6px; }

  .card--front .wordmark {
    left: 50%; top: 50%; transform: translate(-50%, -50%); align-items: center;
  }
  .card--front .wordmark__name { font-size: 104px; color: var(--paper-white); }
  .card--front .wordmark__tagline { font-size: 26px; color: var(--paper-white); }

  .back__curve { position: absolute; inset: 0; width: 100%; height: 100%; }
  .card--back .wordmark { left: 34px; top: 92px; align-items: flex-start; }
  .card--back .wordmark__name { font-size: 88px; color: var(--accent-orange); }
  .card--back .wordmark__tagline { font-size: 19px; color: var(--paper-white); }

  .contact {
    position: absolute; right: 40px; top: 92px; text-align: right;
    font-size: 17px; line-height: 1.3;
  }
  .contact__name { font-weight: 600; font-size: 21px; }
  .contact__role { font-size: 16px; margin-bottom: 18px; }
  .contact__address { margin-bottom: 22px; }
  .contact__line { display: flex; justify-content: flex-end; align-items: center; gap: 8px; }
  .contact__icon { width: 13px; height: 13px; fill: var(--paper-white); }
</style>
</head>
<body>
<main class="canvas">
  <section class="card card--front" aria-label="Card front">
    <div class="wordmark">
      <span class="wordmark__name">RIN</span>
      <span class="wordmark__tagline">Ridgeline insulate co</span>
    </div>
  </section>

  <section class="card card--back" aria-label="Card back">
    <svg class="back__curve" viewBox="0 0 640 366" preserveAspectRatio="none" aria-hidden="true">
      <path d="M0,0 H356 C420,100 405,270 262,366 H0 Z" fill="var(--ink-black)"/>
      <path d="M0,0 H348 C410,100 396,268 250,366 H0 Z" fill="var(--accent-orange)"/>
      <path d="M0,0 H326 C388,98 372,262 224,366 H0 Z" fill="var(--ink-black)"/>
    </svg>
    <div class="wordmark">
      <span class="wordmark__name">RIN</span>
      <span class="wordmark__tagline">Ridgeline insulate co</span>
    </div>
    <div class="contact">
      <p class="contact__name">Dorian Hesketh</p>
      <p class="contact__role">Owner</p>
      <p class="contact__address">482 tilden oak rd Fenwick<br>fl 32390</p>
      <p class="contact__line">8505550147
        <svg class="contact__icon" viewBox="0 0 24 24" aria-hidden="true"><path d="M6.6 10.8a15.1 15.1 0 0 0 6.6 6.6l2.2-2.2a1 1 0 0 1 1-.25 11.4 11.4 0 0 0 3.6.57 1 1 0 0 1 1 1V20a1 1 0 0 1-1 1A17 17 0 0 1 3 4a1 1 0 0 1 1-1h3.5a1 1 0 0 1 1 1c0 1.25.2 2.45.57 3.57a1 1 0 0 1-.25 1z"/></svg>
      </p>
      <p class="contact__line">ridgelineinsulate@mailbox.test
        <svg class="contact__icon" viewBox="0 0 24 24" aria-hidden="true"><path d="M2 5h20v14H2z M3.5 6.5 12 13l8.5-6.5" fill="var(--paper-white)" stroke="var(--brand-blue)" stroke-width="1.5"/></svg>
      </p>
    </div>
  </section>
</main>
</body>
</html>
```